Bref créative
Business Cards, Stationery and Email signature for Luxury Brand
Kestral
I need double sided standard sized Business Card [3.5" x 2"]
Can use whatever font will look high end
Professional
Dennis L. Farrow
CEO/President
417 Larkspur Ave.
Suite 350
Beverly Hills, CA 90187
df@kestralinquiries.example
kestralinquiries.example
Please put in holder for this - Don't have number yet
Want to have plastic business card. All black on front of card with just logo. Back of Card will have all information. Black border on back might be nice showing starburst from logo on top and having line under logo on bottom border of card. Open to other ideas for back as well.
ALL INFORMATION WILL GO ON BACK OF CARD - Card will be plastic
Logo only on front

```html
<!DOCTYPE html>
<html lang="en">
<head>
<meta charset="utf-8">
<title>Kestral Envelope</title>
<link rel="stylesheet" href="https://fonts.googleapis.com/css2?family=Source+Sans+3:wght@400;600;700&display=swap">
<style>
  :root {
    --page-bg: #d9d9d9;
    --paper: #ffffff;
    --ink: #000000;
    --ink-soft: #1a1a1a;
    --fold-line: #e6e6e6;
    --reverse-text: #ffffff;
  }
  * { margin: 0; padding: 0; box-sizing: border-box; }
  html, body {
    width: 1200px;
    height: 878px;
    overflow: hidden;
    background: var(--page-bg);
    font-family: "Source Sans 3", Arial, sans-serif;
  }
  .canvas {
    position: relative;
    width: 1200px;
    height: 878px;
  }

  /* Envelope back with flap */
  .envelope-back {
    position: absolute;
    left: 24px;
    top: 38px;
    width: 1128px;
    height: 360px;
    background: var(--paper);
    box-shadow: 0 6px 18px rgba(0,0,0,0.25);
    overflow: hidden;
  }
  .envelope-back svg {
    position: absolute;
    inset: 0;
  }
  .flap-url {
    position: absolute;
    top: 34px;
    left: 0;
    width: 100%;
    text-align: center;
    color: var(--reverse-text);
    font-size: 19px;
    font-weight: 400;
    letter-spacing: 0.2px;
  }

  /* Envelope front with address */
  .envelope-front {
    position: absolute;
    left: 271px;
    top: 449px;
    width: 905px;
    height: 379px;
    background: var(--paper);
    box-shadow: 0 6px 18px rgba(0,0,0,0.25);
    overflow: hidden;
  }
  .header-band {
    position: absolute;
    left: 0;
    top: 0;
    width: 100%;
    height: 116px;
    background: linear-gradient(90deg, var(--ink) 0%, var(--ink-soft) 48%, #777 72%, var(--paper) 96%);
  }
  .brand-name {
    position: absolute;
    left: 20px;
    top: 50px;
    color: var(--reverse-text);
    font-size: 30px;
    font-weight: 600;
    letter-spacing: 3px;
    text-transform: uppercase;
  }
  .return-address {
    position: absolute;
    left: 53px;
    top: 127px;
    color: var(--ink);
    font-size: 12.5px;
    font-weight: 700;
    line-height: 17px;
    text-transform: uppercase;
    font-style: normal;
  }
</style>
</head>
<body>
<main class="canvas">
  <section class="envelope-back">
    <svg width="1128" height="360" viewBox="0 0 1128 360" aria-hidden="true">
      <line x1="0" y1="0" x2="520" y2="250" stroke="var(--fold-line)" stroke-width="1.5"/>
      <line x1="1128" y1="0" x2="610" y2="250" stroke="var(--fold-line)" stroke-width="1.5"/>
      <line x1="0" y1="360" x2="400" y2="150" stroke="var(--fold-line)" stroke-width="1.5"/>
      <line x1="1128" y1="360" x2="730" y2="150" stroke="var(--fold-line)" stroke-width="1.5"/>
      <path d="M0 0 H1128 V6 C1110 60 1090 70 1040 72 C900 74 720 80 610 120 C580 130 548 130 518 120 C408 80 228 74 88 72 C38 70 18 60 0 6 Z" fill="var(--ink)"/>
    </svg>
    <p class="flap-url">www.kestralinquiries.example</p>
  </section>

  <section class="envelope-front">
    <div class="header-band">
      <span class="brand-name">Kestral</span>
    </div>
    <address class="return-address">
      417 Larkspur Ave.<br>
      Suite 350<br>
      Beverly Hills, CA 90187
    </address>
  </section>
</main>
</body>
</html>
```